Property casualty insurance consultant. Review business insurance plans and provide risk mgmt advice

Front side: logo, tag line, name and info
Back side: Services

Front:
Marcus T. Hollis
Property / Casualty Insurance Consulting and Training
P.O. Box 7385
Maple Ridge, NC 27599
marcus@brindlecrestpartners.example 336-555-0147 www.brindlecrestpartners.example
Back side:
Insurance Program Review
Renewal Proposal Review
Safety Planning / Loss Control
Disaster Planning
Claims Assistance
Updates

Images uploaded. I am non tech so let me know if this did not work. Choose image with Blue Fonts and Orange design element. The brief has also changed to put all info on front and services on back. Thank you.

Reason: took a while to get images downloaded

Going through elimination process. Thanks to all. On any revisions, please add two more services on reverse: Company Training . Agency Training

Target Market(s)

Business owners of all sizes and types

Industry/Entity Type

Insurance

Requirements
Must have
• Logo will have the colors to use, info fonts probably black and should closely match that in logo. Front side, logo, tag line, name and info. Back side with services and logo design element incorporated somehow

```html
<!DOCTYPE html>
<html lang="en">
<head>
<meta charset="utf-8">
<title>Brindlecrest Partners – Business Cards</title>
<link rel="stylesheet" href="https://fonts.googleapis.com/css2?family=Lato:wght@400;700;900&display=swap">
<style>
  :root {
    --navy: #1d2f6b;
    --royal: #143c8c;
    --royal-dark: #0f2f72;
    --orange: #e2701c;
    --amber: #f4b41a;
    --paper: #fbfbfb;
    --ground: #2b2b2d;
    --white: #ffffff;
  }
  * { box-sizing: border-box; margin: 0; padding: 0; }
  html, body { width: 1200px; height: 900px; overflow: hidden; }
  body {
    background: var(--ground);
    font-family: "Lato", Arial, sans-serif;
    position: relative;
  }
  .card {
    position: absolute;
    width: 560px;
    height: 320px;
    overflow: hidden;
    box-shadow: 0 10px 30px rgba(0,0,0,.45);
  }

  /* Back side: services */
  .card-back { left: 60px; top: 90px; display: flex; background: var(--royal); }
  .back-brand {
    width: 180px;
    background: linear-gradient(180deg, var(--amber), var(--orange));
    position: relative;
    display: flex;
    align-items: center;
    justify-content: center;
  }
  .back-brand::after {
    content: "";
    position: absolute;
    right: 8px; top: 0; bottom: 0;
    width: 14px;
    border-left: 3px solid var(--white);
    border-right: 3px solid var(--white);
  }
  .back-brand .brand-name {
    writing-mode: vertical-rl;
    transform: rotate(180deg);
    font-size: 26px;
    font-weight: 700;
    color: var(--navy);
    letter-spacing: 1px;
  }
  .services {
    list-style: none;
    flex: 1;
    background: linear-gradient(135deg, var(--royal), var(--royal-dark));
    padding: 56px 0 0 56px;
  }
  .services li {
    color: var(--white);
    font-weight: 900;
    font-size: 17px;
    letter-spacing: .5px;
    text-transform: uppercase;
    line-height: 26px;
    display: flex;
    align-items: center;
  }
  .services li::before {
    content: "";
    width: 9px; height: 9px;
    border-radius: 50%;
    background: var(--amber);
    margin-right: 14px;
  }

  /* Front side: contact */
  .card-front { left: 580px; top: 490px; background: var(--paper); }
  .front-logo {
    position: absolute; left: 34px; top: 40px;
    display: flex; align-items: center; gap: 10px;
  }
  .front-logo .mark { width: 16px; height: 16px; background: var(--orange); }
  .front-logo .brand-name { font-size: 24px; font-weight: 700; color: var(--navy); }
  .rule {
    position: absolute; left: 34px; right: 26px; top: 82px;
    height: 2px;
    background: linear-gradient(90deg, rgba(226,112,28,.15), var(--orange) 60%, rgba(226,112,28,.2));
  }
  .person-name {
    position: absolute; right: 26px; top: 26px;
    color: var(--orange); font-weight: 900; font-size: 17px;
    text-transform: uppercase; letter-spacing: .5px;
  }
  .tagline {
    position: absolute; right: 26px; top: 92px; text-align: right;
    color: var(--navy); font-weight: 700; font-size: 14px;
    text-transform: uppercase; line-height: 18px;
  }
  .address {
    position: absolute; right: 26px; top: 170px; text-align: right;
    color: var(--navy); font-weight: 900; font-size: 16px; line-height: 22px;
  }
  .contact { position: absolute; left: 34px; bottom: 26px; color: var(--navy); }
  .contact .line { display: flex; align-items: center; gap: 10px; font-size: 15px; font-weight: 700; line-height: 26px; }
  .contact svg { width: 14px; height: 14px; fill: var(--navy); }
  .contact .web { font-size: 16px; font-weight: 900; margin-top: 4px; }
</style>
</head>
<body>

<section class="card card-back" aria-label="Business card back: services">
  <div class="back-brand"><span class="brand-name">Brindlecrest Partners</span></div>
  <ul class="services">
    <li>Agency Training</li>
    <li>Company Training</li>
    <li>Loss Control</li>
    <li>Safety Planning</li>
    <li>Claims Assistance</li>
    <li>Disaster Planning</li>
    <li>Insurance Program Review</li>
    <li>Renewal Proposal Review</li>
  </ul>
</section>

<section class="card card-front" aria-label="Business card front: contact details">
  <div class="front-logo"><span class="mark"></span><span class="brand-name">Brindlecrest Partners</span></div>
  <div class="person-name">Marcus T. Hollis</div>
  <div class="rule"></div>
  <div class="tagline">Property / Casualty<br>Insurance Consulting &amp; Training</div>
  <div class="address">P.O. Box 7385<br>Maple Ridge, NC 27599</div>
  <div class="contact">
    <div class="line">
      <svg viewBox="0 0 16 16" aria-hidden="true"><path d="M1 5c0-2 2-3 7-3s7 1 7 3v1h-4V5H5v1H1z"/><rect x="3" y="8" width="10" height="6" rx="1"/></svg>
      <span>336-555-0147</span>
    </div>
    <div class="line">
      <svg viewBox="0 0 16 16" aria-hidden="true"><path d="M1 3h14v10H1z M2 4l6 5 6-5" stroke="#fbfbfb" stroke-width="1"/></svg>
      <span>marcus@brindlecrestpartners.example</span>
    </div>
    <div class="line web">www.brindlecrestpartners.example</div>
  </div>
</section>

</body>
</html>
```